Sleek Arc website Laser Like Lipo and Facial Rejuvenation busines

I need a website for my Laser Like Lipo and Facial Rejuvenation business called Sleek Arc. I purchased the domain name. I have a logo and before and after pictures to include along with basic information about the procedure and pricing information. I would like my website to be used by customers to be able to schedule appointments. My logo and before-and-after pictures are attached.

My business is called Sleek Arc. It is a laser like Lipo and facial rejuvenation. I've attached my logo and before and after pictures to use on the website.

These treatments are non invasive and people lose 2-10 inches per treatment. My primary audience will be overweight women 30 years of age or older or those with cellulite. I will have some male customers too but mostly women.

As for the web design, I've never had a website before so I really don't have anything specific in mind. I'm open to considering anything. I'm not a girly, girl and I don't like frilly, fancy stuff. I just want something simple but not to either. I love my logo. That is a great fit for my business and personality. I have increased the budget to include coding.

I do not like pastel colors. I do need colors that compliment my logo.

Target Market(s)

Mostly over weight Women or those with cellulite ages 30 and above. Some men.

Industry/Entity Type

Business

Coding

Coded - Design and coding required

Number of Pages Required

3 page

Font styles to use
Serif

Requirements
Must have
• I want my logo and information section on one page, a page for before and after pictures that enlarge when clicked on. I do not want a slide show, and a page for prices. I previously mentioned a section for them to schedule appointments but have decided that I don't want that.
• I do not like pastel colors. I do need colors that compliment my logo.
Should not have
• Not a slide show

```html
<!DOCTYPE html>
<html lang="en">
<head>
<meta charset="utf-8">
<title>Sleek Arc — Laser Lipo &amp; Facial Rejuvenation</title>
<link rel="stylesheet" href="https://fonts.googleapis.com/css2?family=Roboto+Slab:wght@400;500;700;900&family=PT+Serif:wght@400;700&display=swap">
<style>
:root{
  --red:#b3111b;
  --red-dark:#8c0b13;
  --ink:#1e1e1e;
  --text:#555;
  --muted:#888;
  --light:#f2f2f2;
  --band:#161616;
  --footer:#3b3b3b;
  --footer-dark:#2c2c2c;
  --white:#fff;
}
*{margin:0;padding:0;box-sizing:border-box}
html,body{width:1200px;height:2400px;overflow:hidden;background:var(--white)}
body{font-family:"PT Serif",Georgia,serif;color:var(--text);position:relative}
h1,h2,h3,h4,.brand,.nav a,.btn,.service-label,.step-num{font-family:"Roboto Slab",Georgia,serif}
.page{position:relative;width:1200px;height:2400px}

/* header */
.site-header{height:152px;position:relative;padding:0 100px;display:flex;align-items:center;justify-content:space-between}
.brand{display:flex;flex-direction:column}
.brand-name{font-size:52px;font-weight:700;color:var(--red);line-height:1}
.brand-tag{margin-top:8px;font-size:12px;font-weight:700;color:var(--ink);letter-spacing:1px}
.contact-strip{display:flex;gap:64px}
.contact-item{display:flex;align-items:center;gap:16px}
.contact-icon{width:34px;height:34px;background:var(--red);display:flex;align-items:center;justify-content:center}
.contact-label{font-size:14px;color:var(--muted)}
.contact-value{font-size:20px;color:var(--ink);font-weight:700}

/* nav */
.nav{height:46px;background:var(--ink);display:flex;padding-left:100px}
.nav a{color:var(--white);text-decoration:none;font-size:16px;font-weight:500;padding:0 30px;line-height:46px}
.nav a.active{background:#000}

/* hero */
.hero{position:relative;height:540px;background:linear-gradient(90deg,#ececec,#fafafa 60%,#f3f3f3);overflow:hidden}
.hero-photo{position:absolute;left:0;top:0;width:640px;height:520px;background:radial-gradient(ellipse at 45% 45%,#e7c2ab 0%,#d7a98f 35%,#c6c9cf 70%,#e9e9e9 100%)}
.hero-copy{position:absolute;left:740px;top:170px}
.hero-title{font-size:64px;font-weight:900;color:var(--red);line-height:1}
.hero-tag{margin-top:14px;font-size:16px;font-weight:700;color:var(--ink);letter-spacing:.5px}
.btn{display:inline-flex;align-items:stretch;margin-top:28px;height:52px;background:var(--ink);color:var(--white);font-size:21px;font-weight:700;text-decoration:none}
.btn span{padding:0 22px;line-height:52px}
.btn i{width:52px;background:var(--red);display:flex;align-items:center;justify-content:center}
.hero-swoop{position:absolute;left:0;bottom:0;width:1200px;height:120px}

/* service cards */
.services{display:flex;gap:40px;padding:50px 100px 0}
.service-card{width:320px;height:260px;position:relative}
.service-img{position:absolute;inset:0}
.service-label{position:absolute;left:0;right:0;bottom:0;height:60px;background:linear-gradient(180deg,var(--red),var(--red-dark));color:var(--white);font-size:23px;font-weight:700;display:flex;align-items:center;justify-content:center;border-radius:40px 40px 0 0/14px 14px 0 0}

/* about */
.about{position:absolute;top:1100px;left:0;width:1200px;height:420px;background:var(--light)}
.about-photo{position:absolute;left:100px;top:10px;width:320px;height:410px;background:linear-gradient(180deg,#ece5e0,#dcd3cc 40%,#f1f1f1)}
.about-copy{position:absolute;left:480px;top:36px;width:620px}
.about-copy h2{font-size:30px;color:var(--red);font-weight:700}
.about-copy h3{font-size:23px;color:var(--ink);font-weight:400;margin-top:2px}
.about-copy p{font-size:15px;line-height:1.7;margin-top:14px}
.checks{list-style:none;margin-top:16px}
.checks li{font-size:15px;display:flex;align-items:center;gap:12px;margin-bottom:11px}
.checks strong{color:var(--red)}

/* gallery */
.gallery{position:absolute;top:1530px;left:0;width:1200px;height:250px;background:linear-gradient(180deg,#222,var(--band))}
.gallery h2{position:absolute;left:100px;top:26px;font-size:28px;color:var(--white);font-weight:500}
.thumbs{position:absolute;left:100px;top:90px;display:flex;gap:20px}
.thumb{width:184px;height:140px;border:3px solid var(--white);background:linear-gradient(180deg,#e6e2dd,#d9b7a0 50%,#cfc9c5)}

/* unique + testimonial */
.info-row{position:absolute;top:1840px;left:100px;width:1000px;display:flex;justify-content:space-between}
.col{width:460px}
.col h2{font-size:28px;color:var(--red);font-weight:700}
.col h3{font-size:23px;color:var(--ink);font-weight:400;margin-top:2px}
.rule{width:60px;height:3px;background:var(--red);margin-top:12px}
.step{display:flex;gap:20px;margin-top:24px;align-items:flex-start}
.step-num{flex:none;width:42px;height:42px;border-radius:50%;background:var(--ink);color:var(--white);font-weight:700;font-size:18px;display:flex;align-items:center;justify-content:center}
.step p{font-size:15px;line-height:1.6}
.view-all{display:block;margin-top:18px;font-size:14px;color:var(--red);font-weight:700}
.quote{display:flex;gap:22px;margin-top:24px}
.quote-photo{flex:none;width:110px;height:130px;background:linear-gradient(180deg,#e8dcd3,#cfa78e 60%,#ddd)}
.quote p{font-size:15px;line-height:1.6;border-left:3px solid #ddd;padding-left:18px}

/* footer */
.site-footer{position:absolute;left:0;top:2180px;width:1200px;height:220px;background:var(--footer);color:#ddd;padding:20px 100px 0;display:flex;justify-content:space-between}
.site-footer h4{font-size:23px;font-weight:500;color:var(--white);padding-bottom:10px;border-bottom:1px solid #666;margin-bottom:18px}
.foot-col{width:290px}
.foot-line{display:flex;gap:12px;align-items:flex-start;font-size:14px;line-height:1.5;margin-bottom:12px}
.foot-line svg{flex:none;width:16px;height:16px;margin-top:2px}
.hours{width:100%;border-collapse:collapse;font-size:14px}
.hours td{padding:8px 0;border-bottom:1px solid #555}
.hours td:first-child{background:var(--red);color:var(--white);padding-left:10px;width:50%}
.hours td:last-child{padding-left:12px}
.signup{display:flex;height:40px}
.signup span{flex:1;background:var(--footer-dark);color:#bbb;font-size:14px;padding:0 14px;line-height:40px}
.signup b{background:var(--red);color:var(--white);font-weight:700;font-size:14px;padding:0 18px;line-height:40px}
.copyright{margin-top:16px;font-size:13px;color:#ccc;line-height:1.5}
</style>
</head>
<body>
<div class="page">

<header class="site-header">
  <div class="brand">
    <span class="brand-name">Sleek Arc</span>
    <span class="brand-tag">LASER LIPO &amp; FACIAL REJUVENATION</span>
  </div>
  <div class="contact-strip">
    <div class="contact-item">
      <span class="contact-icon"><svg width="20" height="14" viewBox="0 0 20 14"><rect x="1" y="1" width="18" height="12" fill="none" stroke="#fff" stroke-width="2"/><path d="M1 1l9 7 9-7" fill="none" stroke="#fff" stroke-width="2"/></svg></span>
      <div><div class="contact-label">Email:</div><div class="contact-value">info@sleekarc.com</div></div>
    </div>
    <div class="contact-item">
      <span class="contact-icon"><svg width="16" height="20" viewBox="0 0 16 20"><rect x="2" y="1" width="12" height="18" rx="2" fill="none" stroke="#fff" stroke-width="2"/><circle cx="8" cy="15.5" r="1.3" fill="#fff"/></svg></span>
      <div><div class="contact-label">Phone:</div><div class="contact-value">+801 555 0142</div></div>
    </div>
  </div>
</header>

<nav class="nav">
  <a class="active" href="#">Home</a><a href="#">Prices</a><a href="#">Gallery</a><a href="#">Testimonial</a><a href="#">Contact</a>
</nav>

<section class="hero">
  <div class="hero-photo" role="img" aria-label="Photo of a woman's slim waist and hips after body contouring"></div>
  <div class="hero-copy">
    <h1 class="hero-title">SLEEK ARC</h1>
    <div class="hero-tag">LASER LIPO &amp; FACIAL REJUVENATION</div>
    <a class="btn" href="#"><span>Request Appointment</span><i><svg width="22" height="16" viewBox="0 0 22 16"><path d="M1 8h18M12 1l7 7-7 7" fill="none" stroke="#fff" stroke-width="3"/></svg></i></a>
  </div>
  <svg class="hero-swoop" viewBox="0 0 1200 120" preserveAspectRatio="none">
    <path d="M0 40 C300 120 800 120 1200 30 L1200 120 L0 120Z" fill="#fff"/>
    <path d="M0 40 C300 120 800 120 1200 30 L1200 48 C800 130 300 125 0 60Z" fill="#b3111b"/>
  </svg>
</section>

<section class="services">
  <div class="service-card">
    <div class="service-img" role="img" aria-label="Photo of a hand pinching skin at the waist" style="background:linear-gradient(160deg,#f0ddd0,#d8a98c 55%,#b98b72)"></div>
    <div class="service-label">Medical Aesthetics</div>
  </div>
  <div class="service-card">
    <div class="service-img" role="img" aria-label="Before and after photos of a woman's midsection" style="background:linear-gradient(90deg,#d5a58a,#e8cdbb 50%,#cfa088)"></div>
    <div class="service-label">Before &amp; After</div>
  </div>
  <div class="service-card">
    <div class="service-img" role="img" aria-label="Photo of a smiling woman after facial treatment" style="background:linear-gradient(160deg,#e9e1da,#d4ab93 50%,#8a6a5a)"></div>
    <div class="service-label">Cosmetic Surgery</div>
  </div>
</section>

<section class="about">
  <div class="about-photo" role="img" aria-label="Photo of the doctor in a white coat with a stethoscope"></div>
  <div class="about-copy">
    <h2>About</h2>
    <h3>Dr. Nadia Carver</h3>
    <p>Our clinic offers gentle laser treatments that shape the body and refresh the skin without surgery or downtime. Each plan is built around your goals, and most clients see visible inches lost after a single visit. We guide you through every step with honest advice.</p>
    <ul class="checks">
      <li><svg width="14" height="12" viewBox="0 0 14 12"><path d="M1 6l4 4 8-9" fill="none" stroke="#b3111b" stroke-width="2.5"/></svg>No needles, no surgery, no recovery time</li>
      <li><svg width="14" height="12" viewBox="0 0 14 12"><path d="M1 6l4 4 8-9" fill="none" stroke="#b3111b" stroke-width="2.5"/></svg>Lose two to ten inches per treatment</li>
      <li><svg width="14" height="12" viewBox="0 0 14 12"><path d="M1 6l4 4 8-9" fill="none" stroke="#b3111b" stroke-width="2.5"/></svg>Body sessions from <strong>&nbsp;$99&nbsp;</strong>, facials from <strong>&nbsp;$79</strong></li>
      <li><svg width="14" height="12" viewBox="0 0 14 12"><path d="M1 6l4 4 8-9" fill="none" stroke="#b3111b" stroke-width="2.5"/></svg>Six-session packages from <strong>&nbsp;$499</strong></li>
    </ul>
  </div>
</section>

<section class="gallery">
  <h2>Our Gallery</h2>
  <div class="thumbs">
    <div class="thumb" role="img" aria-label="Before and after photo of a client's waist"></div>
    <div class="thumb" role="img" aria-label="Before and after photo of a client's hips"></div>
    <div class="thumb" role="img" aria-label="Before and after photo of a client's midsection"></div>
    <div class="thumb" role="img" aria-label="Before and after photo of a client's thighs"></div>
    <div class="thumb" role="img" aria-label="Before and after photo of a client's legs"></div>
  </div>
</section>

<section class="info-row">
  <div class="col">
    <h2>What's Unique</h2>
    <h3>About Our Treatment Protocols</h3>
    <div class="rule"></div>
    <div class="step"><span class="step-num">1</span><p>Every session starts with a full body analysis and a plan made for you.</p></div>
    <div class="step"><span class="step-num">2</span><p>We track your inches after each visit so you can see real progress.</p></div>
    <span class="view-all">View all &raquo;</span>
  </div>
  <div class="col">
    <h2>Client's</h2>
    <h3>Testimonial</h3>
    <div class="rule"></div>
    <div class="quote">
      <div class="quote-photo" role="img" aria-label="Portrait photo of a client"></div>
      <p>I lost six inches in three sessions and felt great the whole time. The staff were kind, direct and never pushy. I recommend this clinic to every friend who asks.</p>
    </div>
    <span class="view-all">View all &raquo;</span>
  </div>
</section>

<footer class="site-footer">
  <div class="foot-col">
    <h4>Contact Details</h4>
    <div class="foot-line"><svg viewBox="0 0 14 18"><path d="M7 17C7 17 1 10 1 6a6 6 0 0112 0c0 4-6 11-6 11z" fill="#b3111b"/><circle cx="7" cy="6" r="2.2" fill="#3b3b3b"/></svg><span>100 W Hillcrest Way Suite 8B<br>Oak Meadow, IL 60010</span></div>
    <div class="foot-line"><svg viewBox="0 0 16 20"><rect x="3" y="1" width="10" height="18" rx="2" fill="#b3111b"/></svg><span>Phone : +801 555 0142</span></div>
    <div class="foot-line"><svg viewBox="0 0 20 14"><rect x="1" y="1" width="18" height="12" fill="#b3111b"/><path d="M1 1l9 7 9-7" fill="none" stroke="#3b3b3b" stroke-width="1.5"/></svg><span>Email : info@sleekarc.com</span></div>
  </div>
  <div class="foot-col">
    <h4>Our Hours</h4>
    <table class="hours">
      <tr><td>Monday To Friday</td><td>9:00am-7:00pm</td></tr>
      <tr><td>Saturday</td><td>10:00am-7:00pm</td></tr>
    </table>
  </div>
  <div class="foot-col">
    <h4>Newsletter Sign Up</h4>
    <div class="signup"><span>Email Address</span><b>Sign Up</b></div>
    <div class="copyright">Copyright 2015 Sleek Arc<br>All Rights Reserved</div>
  </div>
</footer>

</div>
</body>
</html>
```